Brivo Wellness Co Business Card for food and Beverage Wizards & Alchemists

One main business card design for a wellness enterprise which represents two brands. We need one primary card design, for two different employees. The only difference between the cards will be the name, title and phone number for each employee, all other design elements will be same.
I've uploaded the logos for each brand. I have also uploaded a mockup which I made using Google's drawing tool. I can provide example images of business cards we find attractive if you would like some help picturing what we like.
I'm picturing the color splash on the back of the card below the two logos to be a dark burgundy or blue. This may sound a bit silly but the feel of the card and color should look almost like wizard dress robes. Dark emerald green, dark blue and dark burgundy with black undertones and gold lace.

Target Market(s)

Healthy food and beverage industry

Industry/Entity Type

Health And Wellness

Contact Information for Business Card

On one side we would like the business name, location, title of employee, employee name and contact details. On the flip side we would like our two brand logos and a splash of color. We would like the card to have a black font with some gold accents if possible. We would also like the trim of the business card or a middle ply within the card stock to have a color other than white.

Font styles to use
Serif

Colors
ec1f27
0255a3
00a990

Requirements
Must have
• Bold dark colors, happy to provide sample photos of business cards I like from pinterest. Must have a version for two different employees. Must be sharp, modern and chic.
Nice to have
• Thick card stock layer in between the front and back of card that is either black or gold lace or something to make it feel, well let's say to make it feel expensive.
Should not have
• Should not have any cartoon-ey elements. All business.

```html
<!DOCTYPE html>
<html lang="en">
<head>
<meta charset="utf-8">
<title>Brivo Wellness Co – Business Card</title>
<link rel="stylesheet" href="https://fonts.googleapis.com/css2?family=Playfair+Display:wght@600&family=Jost:wght@300;400&display=swap">
<style>
  :root {
    --backdrop: #ececec;
    --card: #ffffff;
    --ink: #5b68a6;
    --ink-soft: #8f98c4;
    --rule: #c9cde3;
    --splash: #5f74b3;
    --mark: #6d6d6d;
  }
  * { margin: 0; padding: 0; box-sizing: border-box; }
  html, body {
    width: 1200px;
    height: 800px;
    overflow: hidden;
    background: var(--backdrop);
  }
  .stage {
    width: 1200px;
    height: 800px;
    display: flex;
    align-items: center;
    justify-content: center;
    gap: 60px;
  }
  .card {
    position: relative;
    width: 490px;
    height: 280px;
    background: var(--card);
    box-shadow: 0 6px 18px rgba(0, 0, 0, 0.12);
  }
  .company-name {
    font-family: "Playfair Display", serif;
    font-weight: 600;
    font-size: 19px;
    color: var(--ink);
    letter-spacing: 0.2px;
  }
  .company-location {
    font-family: "Playfair Display", serif;
    font-weight: 600;
    font-size: 13px;
    color: var(--ink);
    margin-top: 4px;
  }

  /* Front */
  .card-front .brand-block {
    position: absolute;
    left: 0;
    top: 0;
    width: 50%;
    height: 100%;
    display: flex;
    flex-direction: column;
    align-items: center;
    justify-content: center;
    padding-top: 70px;
  }
  .card-front .divider {
    position: absolute;
    left: 50%;
    top: 70px;
    width: 1px;
    height: 130px;
    background: var(--rule);
  }
  .card-front .contact-block {
    position: absolute;
    left: 50%;
    top: 0;
    width: 50%;
    padding-top: 50px;
    display: flex;
    flex-direction: column;
    align-items: center;
    font-family: "Jost", sans-serif;
    color: var(--ink);
    text-align: center;
  }
  .employee-name {
    font-weight: 400;
    font-size: 17px;
    letter-spacing: 0.4px;
  }
  .employee-title {
    font-weight: 300;
    font-size: 9px;
    margin-top: 3px;
    color: var(--ink-soft);
  }
  .employee-phone,
  .employee-email {
    font-weight: 300;
    font-size: 9px;
    color: var(--ink-soft);
  }
  .employee-phone { margin-top: 22px; }
  .employee-email { margin-top: 22px; }

  /* Back */
  .card-back .brand-block {
    position: absolute;
    left: 0;
    top: 0;
    width: 100%;
    height: 100%;
    display: flex;
    flex-direction: column;
    align-items: center;
    justify-content: center;
    padding-top: 20px;
  }
  .sub-brands {
    display: flex;
    gap: 26px;
    margin-top: 16px;
    font-family: "Playfair Display", serif;
    font-weight: 600;
    font-size: 11px;
    color: var(--mark);
  }
  .sub-brand {
    display: flex;
    align-items: center;
    gap: 5px;
  }
  .sub-brand-dot {
    width: 8px;
    height: 8px;
    border-radius: 50%;
    background: var(--mark);
  }
  .color-splash {
    position: absolute;
    right: 30px;
    top: 40px;
    width: 84px;
    height: 84px;
  }
</style>
</head>
<body>
<main class="stage">
  <section class="card card-front" aria-label="Card front">
    <div class="brand-block">
      <p class="company-name">Brivo Wellness Co</p>
      <p class="company-location">Larkvale, CA</p>
    </div>
    <div class="divider"></div>
    <div class="contact-block">
      <p class="employee-name">Owen Marsh</p>
      <p class="employee-title">Beverage Alchemist</p>
      <p class="employee-phone">415.555.0142</p>
      <p class="employee-email">hello@brivowellness.co</p>
    </div>
  </section>

  <section class="card card-back" aria-label="Card back">
    <svg class="color-splash" viewBox="0 0 84 84" role="img" aria-label="Blue ink splash of colour">
      <defs>
        <radialGradient id="splashFill" cx="50%" cy="50%" r="50%">
          <stop offset="0%" stop-color="#5f74b3"/>
          <stop offset="45%" stop-color="#5f74b3"/>
          <stop offset="100%" stop-color="#5f74b3" stop-opacity="0"/>
        </radialGradient>
      </defs>
      <circle cx="42" cy="42" r="42" fill="url(#splashFill)"/>
    </svg>
    <div class="brand-block">
      <p class="company-name">Brivo Wellness Co</p>
      <p class="company-location">Larkvale, CA</p>
      <div class="sub-brands">
        <span class="sub-brand"><span class="sub-brand-dot"></span>Halden</span>
        <span class="sub-brand">Pique</span>
      </div>
    </div>
  </section>
</main>
</body>
</html>
```